Bright Oak Fitness Facility Business Cards

Business Card Design that incorporates the logo and tagline

Target Market(s)

Fitness, People Who Exercise

Contact Information for Business Card

2817 Mossgrove Bend Road
Tavares, Florida 32190
Phone: 352-555-Jump (5867)
www.brightoakfitness.example
info@brightoakfitness.example

Requirements
Must have
• Logo, Address, Website, email and tagline "More Than A Gym". Colors should be red/black/grey/white

```html
<!DOCTYPE html>
<html lang="en">
<head>
<meta charset="utf-8">
<title>Bright Oak Fitness – Business Card</title>
<link rel="stylesheet" href="https://fonts.googleapis.com/css2?family=Montserrat:wght@700&family=Open+Sans:wght@400;600&display=swap">
<style>
  :root {
    --bg: #2a2a2c;
    --card: #ffffff;
    --red: #e8141f;
    --ink: #231f20;
    --grey: #5a5a5a;
    --rule: #b5b5b5;
  }
  * { margin: 0; padding: 0; box-sizing: border-box; }
  html, body { width: 1200px; height: 885px; overflow: hidden; background: var(--bg); }
  .card {
    position: absolute; left: 100px; top: 156px;
    width: 1000px; height: 572px;
    background: var(--card);
    font-family: "Open Sans", Arial, sans-serif;
    color: var(--ink);
    overflow: hidden;
  }
  .brand {
    position: absolute; left: 470px; top: 120px;
    display: flex; align-items: center; gap: 14px;
  }
  .brand-dot { width: 22px; height: 22px; border-radius: 50%; background: var(--red); }
  .brand-name {
    font-family: "Montserrat", Arial, sans-serif; font-weight: 700;
    font-size: 40px; letter-spacing: 1px; color: var(--ink);
  }
  .divider {
    position: absolute; left: 140px; right: 120px; top: 330px;
    height: 1px; background: var(--rule);
  }
  .person { position: absolute; left: 92px; top: 258px; }
  .person-name {
    font-family: "Montserrat", Arial, sans-serif; font-weight: 700;
    font-size: 30px; color: var(--red); letter-spacing: .5px;
  }
  .person-role { font-size: 20px; color: var(--ink); margin-top: 2px; }
  .contact { position: absolute; left: 110px; top: 350px; list-style: none; }
  .contact li {
    display: flex; align-items: center; gap: 12px;
    font-size: 22px; color: var(--grey); line-height: 34px;
  }
  .contact svg { width: 20px; height: 20px; flex: none; }
  .address {
    position: absolute; right: 90px; top: 345px;
    text-align: right; font-size: 21px; line-height: 30px; color: var(--grey);
  }
  .bands { position: absolute; left: 0; bottom: 0; }
  .tagline {
    position: absolute; right: 60px; bottom: 26px;
    font-size: 22px; font-weight: 600; color: #fff;
  }
</style>
</head>
<body>
  <div class="card">
    <div class="brand">
      <span class="brand-dot"></span>
      <span class="brand-name">BRIGHT OAK FITNESS</span>
    </div>

    <div class="person">
      <div class="person-name">MARCUS HALE</div>
      <div class="person-role">PRESIDENT</div>
    </div>

    <div class="divider"></div>

    <ul class="contact">
      <li>
        <svg viewBox="0 0 20 20"><circle cx="10" cy="10" r="10" fill="var(--red)"/><path d="M6 6.5c0-.8.7-1 1.3-1l1.2 2.3-1 1c.6 1.4 1.6 2.4 3 3l1-1 2.3 1.2c0 .6-.2 1.3-1 1.3C9.3 13.3 6.7 10.7 6 6.5z" fill="#fff"/></svg>
        352-555-5867
      </li>
      <li>
        <svg viewBox="0 0 20 20"><circle cx="10" cy="10" r="10" fill="var(--red)"/><rect x="5" y="6.5" width="10" height="7" fill="#fff"/><path d="M5 6.5l5 4 5-4" fill="none" stroke="var(--red)" stroke-width="1"/></svg>
        info@brightoakfitness.example
      </li>
      <li>
        <svg viewBox="0 0 20 20"><circle cx="10" cy="10" r="10" fill="var(--red)"/><circle cx="10" cy="10" r="5" fill="none" stroke="#fff" stroke-width="1.2"/><path d="M5 10h10M10 5c-2 3-2 7 0 10M10 5c2 3 2 7 0 10" fill="none" stroke="#fff" stroke-width="1"/></svg>
        www.brightoakfitness.example
      </li>
    </ul>

    <div class="address">
      2817 Mossgrove Bend Road<br>
      Tavares, Florida 32190
    </div>

    <svg class="bands" width="1000" height="100" viewBox="0 0 1000 100">
      <polygon points="0,76 640,44 640,100 0,100" fill="var(--red)"/>
      <polygon points="662,22 1000,0 1000,100 656,100" fill="var(--red)"/>
    </svg>
    <div class="tagline">More Than A Gym</div>
  </div>
</body>
</html>
```